Medical Marihuana Ziplock Bag Mockup Design

We seek skilled and professional designer for medical marihuana ziplock bag packaging design. We need a modern, minimal, clean Design with the name productname: Plumo - Endproduct will be a ziplock bag (see attachment) samples.
Product may but must not contain a cannabis leaf in Design7Logo

Target Market(s)

young audience

Industry/Entity Type

Medical

Logo Text

P L U M O

Font styles to use
Serif
Sans Serif

Colors
9bcb3c
abd037
cadf82
ffc214
fece3e
fee18a
6b449b
886aae
b8a6cd

Requirements
Nice to have
• Can but must not contain a minimal cannabis leaf as abstract sign

```html
<!DOCTYPE html>
<html lang="de">
<head>
<meta charset="utf-8">
<title>Plumo Endproduct – Beutel</title>
<link rel="stylesheet" href="https://fonts.googleapis.com/css2?family=Exo+2:wght@700;800&family=PT+Sans:wght@400&display=swap">
<style>
  :root{
    --canvas:#f3f3f3;
    --green:#17904a;
    --green-deep:#12803f;
    --pale:#d6e6b0;
    --cream:#f4e9bb;
    --leaf-grey:#5d6563;
    --ink:#151515;
  }
  *{margin:0;padding:0;box-sizing:border-box}
  html,body{width:1200px;height:1200px;overflow:hidden;background:var(--canvas)}
  .canvas{position:relative;width:1200px;height:1200px}

  .bag{position:absolute;top:240px;width:440px;height:720px;border-radius:18px;overflow:hidden}
  .bag--green{left:120px;--top:var(--green);--mid:var(--pale);--accent:var(--green);--toptext:var(--pale);--leaf:var(--leaf-grey);--warntext:var(--pale)}
  .bag--cream{left:640px;--top:var(--cream);--mid:var(--green);--accent:var(--cream);--toptext:var(--green);--leaf:var(--cream);--warntext:var(--green)}

  .bag__top{position:absolute;left:0;top:0;width:100%;height:160px;background:var(--top)}
  .bag__mid{position:absolute;left:0;top:160px;width:100%;height:326px;background:var(--mid)}
  .bag__bottom{position:absolute;left:0;top:486px;width:100%;height:234px;background:var(--top)}

  .bag__scallop{position:absolute;left:0;top:160px;width:100%;height:7px;
    background:radial-gradient(circle at 6px 0,var(--top) 4px,transparent 4.6px) repeat-x;
    background-size:12px 7px}

  .origin{position:absolute;top:38px;width:100%;text-align:center;
    font-family:'PT Sans',sans-serif;font-size:22px;letter-spacing:.3px;color:var(--toptext)}

  .badge{position:absolute;left:50%;top:108px;width:120px;height:120px;margin-left:-60px;
    border-radius:50%;background:var(--mid)}

  .wordmark{position:absolute;top:186px;width:100%;text-align:center;
    font-family:'Exo 2',sans-serif;font-weight:800;font-size:56px;line-height:1;letter-spacing:1px;color:var(--accent)}
  .subline{position:absolute;top:250px;width:100%;text-align:center;
    font-family:'Exo 2',sans-serif;font-weight:800;font-size:27px;line-height:1;letter-spacing:.5px;color:var(--accent)}

  .leaf-art{position:absolute;left:70px;top:292px;width:300px;height:250px;
    background:var(--leaf);border-radius:50% 50% 38% 38% / 62% 62% 38% 38%;opacity:.92}

  .warning{position:absolute;left:80px;top:560px;width:280px;height:140px;
    border:4px solid var(--ink);padding:6px 8px;text-align:center;
    font-family:'PT Sans',sans-serif;font-size:13.5px;line-height:18px;color:var(--warntext)}
</style>
</head>
<body>
<main class="canvas">

  <section class="bag bag--green">
    <div class="bag__top"></div>
    <div class="bag__mid"></div>
    <div class="bag__bottom"></div>
    <div class="bag__scallop"></div>
    <p class="origin">100% SCHWEIZER HANF</p>
    <div class="badge"></div>
    <h1 class="wordmark">PLUMO</h1>
    <p class="subline">ENDPRODUCT</p>
    <div class="leaf-art" role="img" aria-label="Large grey hemp leaf illustration"></div>
    <p class="warning">Rauchen fügt Ihnen und den<br>Menschen in Ihrer Umgebung<br>erheblichen Schaden zu. Fumer nuit<br>Gravement à votre santé et à celle<br>de votre entourage.<br>Il fumo danneggia gravemente te e<br>chi ti sta intorno.</p>
  </section>

  <section class="bag bag--cream">
    <div class="bag__top"></div>
    <div class="bag__mid"></div>
    <div class="bag__bottom"></div>
    <div class="bag__scallop"></div>
    <p class="origin">100% SCHWEIZER HANF</p>
    <div class="badge"></div>
    <h1 class="wordmark">PLUMO</h1>
    <p class="subline">ENDPRODUCT</p>
    <div class="leaf-art" role="img" aria-label="Large cream hemp leaf illustration"></div>
    <p class="warning">Rauchen fügt Ihnen und den<br>Menschen in Ihrer Umgebung<br>erheblichen Schaden zu. Fumer nuit<br>Gravement à votre santé et à celle<br>de votre entourage.<br>Il fumo danneggia gravemente te e<br>chi ti sta intorno.</p>
  </section>

</main>
</body>
</html>
```